Webdesign für Hundeerziehungsberatung
Zielgruppe:
Hundehalter, die entweder einen Welpen angeschafft haben, ihren Hund ausbilden oder fördern wollen sowie Menschen mit einem 'Problemhund'.
Die Hundeerziehungsberatung bietet Hundehaltern die Erziehung im Einzelsetting und im Gruppensetting an.
Aufgabenstellung
die Farben sollen sich am Logo orientieren, gern noch eine Farbe dazu. Logo anbei, Bilder anbei. Flyer anbei
Sollten die Bilder ausreichen bitten wir um Auswahl bei pixel.morvani. Tool: Photoshop.
Der Kundin gefällt: https://www.pfotenlauf-brevik.de/

```html
<!DOCTYPE html>
<html lang="de">
<head>
<meta charset="utf-8">
<title>Leinenlicht – Hundeerziehungsberatung</title>
<link rel="stylesheet" href="https://fonts.googleapis.com/css2?family=Lato:wght@300;400;700;900&display=swap">
<style>
:root{
  --brown:#8b7b6b;
  --brown-dark:#7d6f60;
  --green:#4e6a2e;
  --green-bright:#3f6f1f;
  --bg:#f9f9f9;
  --panel:#e4e3e2;
  --white:#ffffff;
  --text:#8b7b6b;
  --line:#8a8580;
}
*{box-sizing:border-box;margin:0;padding:0}
html,body{width:1200px;height:3351px;overflow:hidden}
body{position:relative;background:var(--bg);font-family:'Lato',sans-serif;color:var(--text)}
.abs{position:absolute}

/* header */
.site-header{left:0;top:0;width:1200px;height:128px;background:var(--bg)}
.brand{display:flex;align-items:center;gap:10px;color:var(--brown);font-size:30px;font-weight:400}
.brand-mark{width:60px;height:60px;border:3px solid var(--brown);border-radius:50%}
.site-header .brand{left:46px;top:26px}
.main-nav{left:541px;top:40px;display:flex;gap:10px;font-size:16.5px;font-weight:700;color:#4a4038}
.dropdown{left:694px;top:83px;width:132px;height:57px;background:var(--brown);border-radius:4px;color:var(--white);font-size:14px;font-weight:700;padding:11px 0 0 12px;line-height:17px}
.dropdown::before{content:"";position:absolute;left:10px;top:-12px;border:7px solid transparent;border-bottom:12px solid var(--brown);border-top:0}

/* hero */
.hero-photo{left:0;top:128px;width:1200px;height:611px;background:linear-gradient(90deg,#b89a62 0%,#c8ab73 35%,#9a9b9a 65%,#a5a39f 100%)}

/* intro */
.intro-title{left:0;top:756px;width:1232px;text-align:center;font-size:49px;font-weight:700;color:var(--brown)}
.intro-text{left:250px;top:849px;width:690px;text-align:center;font-size:13px;font-weight:700;line-height:16.5px}

.card{width:282px;height:390px;background:var(--white);box-shadow:0 2px 10px rgba(0,0,0,.08);text-align:center}
.card-photo{position:absolute;left:14px;top:13px;width:254px;height:175px}
.card h3{position:absolute;left:0;top:210px;width:100%;font-size:26px;font-weight:400;color:var(--brown)}
.card p{position:absolute;left:22px;top:262px;width:242px;text-align:left;font-size:13px;line-height:16px}
.card .btn{position:absolute;left:56px;top:335px;width:166px;height:33px;background:var(--green);color:var(--white);font-size:13px;line-height:33px;border-radius:3px}

/* relation */
.circle{border-radius:50%}
.relation-title{left:700px;top:1557px;width:340px;text-align:center;font-size:44px;font-weight:400;line-height:51px;color:var(--brown)}
.relation-title span{color:var(--green);display:block}

/* events */
.events-photo{left:0;top:2123px;width:598px;height:426px;background:linear-gradient(135deg,#7d7f98 0%,#c9cad6 50%,#8f91a6 100%)}
.events-panel{left:598px;top:2123px;width:602px;height:426px;background:var(--panel)}
.events-title{left:678px;top:2178px;font-size:48px;font-weight:400;color:var(--brown)}
.events-text{left:684px;top:2272px;width:480px;font-size:20px;line-height:25px}
.events-btn{left:788px;top:2421px;width:292px;height:71px;background:var(--brown);color:var(--white);font-size:28px;line-height:71px;text-align:center;border-radius:3px}

/* contact */
.contact-title{left:105px;top:2702px;font-size:49px;line-height:54px;font-weight:700;color:var(--green)}
.contact-title span{display:block;font-weight:400;color:var(--brown)}
.contact-text{left:110px;top:2845px;width:470px;font-size:13px;font-weight:700;line-height:16.5px}
.form-panel{left:648px;top:2662px;width:462px;height:318px;background:#f4f4f4}
.field{background:var(--white);border:1px solid var(--line);border-radius:3px;font-size:10px;color:#b0a9a2;padding:7px 9px}
.consent{left:676px;top:2913px;font-size:10.5px;color:#555;display:flex;align-items:center;gap:4px}
.consent i{width:8px;height:8px;border:1px solid #555;display:inline-block}
.consent b{color:var(--green);font-weight:400}
.submit{left:665px;top:2940px;width:425px;height:28px;background:var(--green-bright);color:var(--white);font-size:19px;text-align:center;line-height:28px;border-radius:2px}

/* footer */
.site-footer{left:0;top:3041px;width:1200px;height:310px;background:var(--brown);border-radius:8px 0 0 0;color:var(--white)}
.site-footer .brand{left:88px;top:50px;color:var(--white)}
.site-footer .brand-mark{border-color:var(--white)}
.foot-head{font-size:11.5px;font-weight:700}
.foot-list{font-size:9.5px;line-height:24px}
.foot-icons{display:flex;flex-direction:column;gap:6px}
</style>
</head>
<body>

<header class="site-header abs">
  <div class="brand abs"><span class="brand-mark"></span>Leinenlicht</div>
  <nav class="main-nav abs">
    <span>Home</span><span>Erstgespräch</span><span>Erziehung</span><span>Kurse</span><span>Veranstaltungen</span><span>Unternehmen</span><span>Kontakt</span>
  </nav>
  <div class="dropdown abs">im Einzelsetting<br>im Gruppensetting</div>
</header>

<div class="hero-photo abs" role="img" aria-label="Foto: Trainerin mit Hund im herbstlichen Gras"></div>

<section>
  <h1 class="intro-title abs">Lorem Ipsum</h1>
  <p class="intro-text abs">Lorem ipsum dolor sit amet, consectetur adipiscing elit, sed do eiusmod tempor incididunt ut labore et dolore magna aliqua. Quis ipsum suspendisse ultrices gravida. Risus commodo viverra maecenas accumsan lacus vel facilisis.</p>

  <article class="card abs" style="left:82px;top:915px">
    <div class="card-photo" role="img" aria-label="Foto: Trainerin mit Hund auf einer Wiese" style="background:linear-gradient(180deg,#3f5a34,#7fa046)"></div>
    <h3>ERSTGESPRÄCH</h3>
    <p>Lorem ipsum dolor sit amet, consectetur adipiscing elit, sed do eiusmod tempor incididunt ut labore et dolore magna</p>
    <div class="btn">JETZT ANFRAGEN</div>
  </article>
  <article class="card abs" style="left:470px;top:915px;height:385px">
    <div class="card-photo" role="img" aria-label="Foto: Training mit Hund im Wald" style="background:linear-gradient(180deg,#8a8a70,#6d7a3c)"></div>
    <h3>ERZIEHUNG</h3>
    <p>Lorem ipsum dolor sit amet, consectetur adipiscing elit, sed do eiusmod tempor incididunt ut labore et dolore magna</p>
    <div class="btn">MEHR ERFAHREN</div>
  </article>
  <article class="card abs" style="left:834px;top:915px;height:385px">
    <div class="card-photo" role="img" aria-label="Foto: Hund auf Holzboden neben Smartphone und Kalender" style="background:linear-gradient(135deg,#c27a3a,#6b3a22 60%,#3a4f8a)"></div>
    <h3>KURSE &amp; TERMINE</h3>
    <p>Lorem ipsum dolor sit amet, consectetur adipiscing elit, sed do eiusmod tempor incididunt ut labore et dolore magna</p>
    <div class="btn" style="top:330px">MEHR ERFAHREN</div>
  </article>
</section>

<section>
  <div class="circle abs" role="img" aria-label="Foto: spielender Hund im Garten" style="left:99px;top:1440px;width:412px;height:412px;background:radial-gradient(circle at 40% 40%,#a58b6e,#3f6a2c)"></div>
  <div class="circle abs" role="img" aria-label="Foto: zweiter Hund beim Spielen auf der Wiese" style="left:330px;top:1520px;width:340px;height:360px;background:radial-gradient(circle at 40% 40%,#5d6a5a,#4f8a32)"></div>
  <h2 class="relation-title abs">Hund Mensch<span>in Beziehung</span></h2>
</section>

<section>
  <div class="events-photo abs" role="img" aria-label="Foto: Ordner mit Beschriftung Workshop und Seminar"></div>
  <div class="events-panel abs"></div>
  <h2 class="events-title abs">Veranstaltungen</h2>
  <p class="events-text abs">Lorem ipsum dolor sit amet, consectetur adipiscing elit, sed do eiusmod tempor incididunt ut labore et dolore magna aliqua. Quis ipsum suspendisse ultrices gravida. Risus commodo viverra maecenas accumsan lacus vel facilisis.</p>
  <div class="events-btn abs">MEHR ERFAHREN</div>
</section>

<section>
  <h2 class="contact-title abs">Interessiert?<span>Dann schreibe mir!</span></h2>
  <p class="contact-text abs">Lorem ipsum dolor sit amet, consectetur adipiscing elit, sed do eiusmod tempor incididunt ut labore et dolore magna aliqua. Quis ipsum suspendisse ultrices gravida. Risus commodo viverra maecenas accumsan lacus vel facilisis.</p>
  <div class="form-panel abs"></div>
  <div class="field abs" style="left:665px;top:2681px;width:203px;height:31px">Vor- und Nachname*</div>
  <div class="field abs" style="left:665px;top:2726px;width:203px;height:31px">Email*</div>
  <div class="field abs" style="left:887px;top:2726px;width:203px;height:31px">Telefonnummer*</div>
  <div class="field abs" style="left:665px;top:2770px;width:425px;height:133px">Nachricht</div>
  <div class="consent abs"><i></i>Die <b>Datenschutzerklärung</b> wurde gelesen und hiermit bestätigt</div>
  <div class="submit abs">Absenden</div>
</section>

<footer class="site-footer abs">
  <div class="brand abs"><span class="brand-mark"></span>Leinenlicht</div>
  <div class="abs" style="left:475px;top:73px">
    <div class="foot-head">KONTAKT</div>
    <div class="foot-icons" style="margin-top:10px">
      <svg width="11" height="11" viewBox="0 0 12 12"><path d="M6 1 1 6h2v5h2.5V8h1v3H9V6h2z" fill="#fff"/></svg>
      <svg width="11" height="12" viewBox="0 0 12 14"><path d="M6 0a4.5 4.5 0 0 0-4.5 4.5C1.5 8 6 14 6 14s4.5-6 4.5-9.5A4.5 4.5 0 0 0 6 0zm0 6.5a2 2 0 1 1 0-4 2 2 0 0 1 0 4z" fill="#fff"/></svg>
      <svg width="11" height="11" viewBox="0 0 12 12"><path d="M2.5 1 4.5 3.5 3.5 5c.8 1.6 2 2.8 3.5 3.5l1.5-1 2.5 2-1 1.5C5.5 11 1 6.5 1 2z" fill="#fff"/></svg>
      <svg width="11" height="11" viewBox="0 0 12 12" style="margin-top:6px"><path d="M3 1h6v3H3zM1 4h10v5H9v2H3V9H1zm3 4v2h4V8z" fill="#fff"/></svg>
    </div>
  </div>
  <div class="abs" style="left:755px;top:73px">
    <div class="foot-head">RECHTLICHES</div>
    <div class="foot-list" style="margin-top:2px">▸ Cookie Richtlinie<br>▸ Impressum<br>▸ Datenschutzerklärung</div>
  </div>
  <div class="abs" style="left:981px;top:73px">
    <div class="foot-head">SOCIAL MEDIA</div>
  </div>
</footer>

</body>
</html>
```